Life Science Backpage Advertisement

We are a local SME distributing life science products in Singapore. The advertisement is to be placed on the backpage of genoview pacific, with over 70,000 readers.
The product to be advertised is a Korvala incubator TRV-42KEX
The MAIN selling point of this unit is its hydrogen peroxide (H2O2) decontamination feature. The idea is that the vaporized H2O2 is a safe and efficient way (3 hours) to decontaminate the chamber. It is safe because H2O2 is reduced to water and oxygen.
Would want the main picture to represent the reduction to water. It could be something along the lines of these pictures in pixelvault.
http://www.pixelvault-example.com/cat.mhtml?searchterm=water+droplets&search_group=&lang=en&search_source=search_form
http://www.pixelvault-example.com/cat.mhtml?lang=en&search_source=search_form&search_tracking_id=A10000AA-0000-00A0-AA00-0AAAAAA0000A&version=llv1&anyorall=all&safesearch=1&searchterm=water+droplets+h20&search_group=&orient=&search_cat=&searchtermx=&photographer_name=&people_gender=&people_age=&people_ethnicity=&people_number=&commercial_ok=&color=&show_color_wheel=1#id=100000000&src=A10000AA-00AA-00A0-0A00-0AAAAAA0000A-1-9
The tag line could be "Decontamination at it's safest"
The write up
"In cell culture, contamination is the worst enemy. Korvala's unique high-speed decontamination system utilizing vaporized H2O2 offers time-saving and documented chamber decontamination with complete safety.
Whole process takes less than 3 hours, versus 14 hours for heat sterilization process.
All interior components are decontaminated in situ. No need for time-consuming removal and autoclaving.
After decontamination H2O2 vapor is decomposed to harmless water and oxygen by UV light.
Other main features of the incubator
"Copper-enriched stainless steel prevents contamination due to it's bacteria-killing property of copper with the corrosion resistance of stainless steel
UV lamp isolated from cell cultures, sterilizes chamber air and water in the humidifying pan, maintaining contamination-free conditions in chamber
Accurate temperature and CO2 level control
Double stackable"
Things to take note of:
Do not want the picture of the device to be too big, refer to sample
Do not want a product flyer, but an advertisement to catch the attention of the users
Bottom portion of the sample advert has to be copied over
Refer to http://www.genoviewpacific-example.com/digital_assets/115/mediakit_2013.pdf for more information on the dimensions, page 11, print magazine under regular advertisements
Target Market(s)
Life science B2B consumers
Industry/Entity Type
Steel
Look and feel

```html
<!DOCTYPE html>
<html lang="en">
<head>
<meta charset="utf-8">
<title>Korvala TRV-42KEX – 0% Bacteria</title>
<link rel="stylesheet" href="https://fonts.googleapis.com/css2?family=Anton&family=Arimo:wght@400;700&display=swap">
<style>
  :root {
    --water-deep: #1d4664;
    --water-mid: #2f6f98;
    --water-light: #4b90bb;
    --brand-blue: #1e6bb5;
    --band-blue: #2a74b9;
    --body-text: #222222;
    --footer-text: #7a7a7a;
    --panel-top: #ffffff;
    --panel-bottom: #e6e6e6;
    --cabinet-light: #ece6d4;
    --cabinet-shade: #bdb6a3;
  }
  html, body {
    margin: 0;
    padding: 0;
    overflow: hidden;
    background: #ffffff;
  }
  .advert {
    position: relative;
    width: 1200px;
    height: 890px;
    overflow: hidden;
    font-family: "Arimo", Arial, sans-serif;
    background: linear-gradient(180deg, var(--panel-top) 66%, var(--panel-bottom) 100%);
  }
  .hero {
    position: absolute;
    left: 0;
    top: 0;
    width: 1200px;
    height: 586px;
    background:
      radial-gradient(ellipse at 30% 20%, rgba(110,170,210,0.35), transparent 60%),
      linear-gradient(180deg, var(--water-mid) 0%, var(--water-deep) 45%, var(--water-light) 100%);
  }
  .hero-headline {
    position: absolute;
    left: 0;
    top: 0;
    width: 1200px;
    height: 586px;
  }
  .hero-headline text {
    font-family: "Anton", "Arial Narrow", sans-serif;
  }
  .divider-band {
    position: absolute;
    left: 0;
    top: 586px;
    width: 1200px;
    height: 6px;
    background: var(--band-blue);
  }
  .product-visual {
    position: absolute;
    left: 944px;
    top: 536px;
    width: 194px;
    height: 232px;
    border-radius: 4px;
    background: linear-gradient(90deg, var(--cabinet-shade) 0%, var(--cabinet-light) 25%, var(--cabinet-light) 80%, var(--cabinet-shade) 100%);
    box-shadow: 0 4px 10px rgba(0,0,0,0.18);
  }
  .body-copy {
    position: absolute;
    left: 36px;
    top: 606px;
    width: 900px;
    color: var(--body-text);
    font-size: 16.8px;
    line-height: 21.6px;
    white-space: nowrap;
  }
  .body-copy p {
    margin: 0 0 6px 0;
  }
  .brand-name {
    position: absolute;
    left: 36px;
    top: 748px;
    margin: 0;
    font-size: 54px;
    line-height: 60px;
    font-weight: 700;
    letter-spacing: -0.5px;
    color: var(--brand-blue);
  }
  .feature-badges {
    position: absolute;
    left: 342px;
    top: 768px;
    display: flex;
    gap: 8px;
    margin: 0;
    padding: 0;
    list-style: none;
  }
  .feature-badges li {
    width: 32px;
    height: 32px;
    border-radius: 3px;
    background: linear-gradient(180deg, #5aa2dd, #2f7cc2);
    box-shadow: inset 0 0 0 1px rgba(255,255,255,0.35);
  }
  .distributor-info {
    position: absolute;
    left: 36px;
    top: 815px;
    width: 900px;
    color: var(--footer-text);
    font-size: 10px;
    line-height: 15px;
  }
  .distributor-info p {
    margin: 0;
  }
  .distributor-info p:last-child {
    margin-top: 3px;
  }
</style>
</head>
<body>
<main class="advert">
  <section class="hero" role="img" aria-label="Close-up photograph of water droplets on a blue rippled surface">
    <svg class="hero-headline" viewBox="0 0 1200 586" xmlns="http://www.w3.org/2000/svg" aria-label="0% Bacteria">
      <defs>
        <linearGradient id="letterFill" x1="0" y1="0" x2="0" y2="1">
          <stop offset="0" stop-color="#a9dbf6"/>
          <stop offset="0.5" stop-color="#6cbbe8"/>
          <stop offset="1" stop-color="#4da6dc"/>
        </linearGradient>
      </defs>
      <text x="74" y="246" font-size="212" fill="url(#letterFill)" textLength="322" lengthAdjust="spacingAndGlyphs">0%</text>
      <text x="74" y="446" font-size="223" fill="url(#letterFill)" textLength="1060" lengthAdjust="spacingAndGlyphs">BACTERIA</text>
    </svg>
  </section>

  <div class="divider-band"></div>

  <div class="product-visual" role="img" aria-label="Korvala TRV-42KEX CO2 incubator, beige cabinet with front control panel"></div>

  <section class="body-copy">
    <p>In cell culture, contamination is the worst enemy. Korvala's unique high-speed decontamination system<br>utilizing vaporized H2O2 offers time-saving and documented chamber decontamination with complete safety.<br>Whole process takes less than 3 hours, versus 14 hours for heat sterilization process.</p>
    <p>All interior components are decontaminated in situ. No need for time-consuming removal and autoclaving.<br>After decontamination H2O2 vapor is decomposed to harmless water and oxygen by UV light.</p>
  </section>

  <h2 class="brand-name">Korvala</h2>

  <ul class="feature-badges" aria-label="Feature badges">
    <li></li><li></li><li></li><li></li><li></li><li></li><li></li>
    <li></li><li></li><li></li><li></li><li></li><li></li>
  </ul>

  <footer class="distributor-info">
    <p>Master distributor of Korvala Biomedical Products (South-East Asia/South Asia) Verida Lab Supply (Asia) Pte Ltd</p>
    <p>48 Kestrel Loop #05-02 Harbourtech Hub Singapore 100048 Telephone: (65) 6000 1200 Fax: (65) 6000 1201 Email: sales@veridalab-example.sg Verida Lab Supply India Pvt Ltd</p>
    <p>B-210 Lotus Chambers Ring Road Sector 9 New Delhi 110 009 Tel: +91-11-40000100 Fax: +91-11-40000101 Email: india@veridalab-example.sg</p>
  </footer>
</main>
</body>
</html>
```